Banner-Design für Verkauf von Organic und fair Trade Mode
Zielgruppe
Wir starten einen Internetshop mit dem Verkauf von Organic und fair Trade Mode. Mit eigenen Designs aber wir verkaufen auch die Ware ohne Design.
Ein Shirt Designer ist angeschlossen so dass die Kunden auch die Shirts selbst gestalten können.
1. Textildruck Service
2. Verkauf von bedruckten und unbedruckten Shirts
3. Kunden können jedes Kleidungsstück im Shop individualisieren
Aufgabenstellung
Wir benötigen 4 Banner für unseren Shop. Die Bilder sollen über die komplette breite der Startseite des Shops gehen. Plan ist es die Banner in einem Slider nach einander laufen zu lassen.
1. Banner der auf unseren Printservice auch für Firmen, Schulen, Vereine etc. hinweist
2.Jedes Shirt kann selbst gestaltet werden
3. Hinweisbanner auf Fair Trade und Organic Kategorien im Shop
4. Banner für anstehende SALE und permanente Mengenrabatt Aktionen
5. Drucktechniken
Größe: 1240 * 400 px and smaller like 900 * ~ 400px.
Als Dateien sind das Firmenlogo sowie das Logo unsers Labels beigefügt außerdem ist ein Banner der jedoch nicht professionell genug ist angehängt.
Farbgebung des Shops: Header und navigation schwarz / grau,
Daher sind wir für alle Vorschläge offen und würden die Zusammenarbeit gerne weiter ausbauen da wir dringend Grafiker / Designer benötigen.

```html
<!DOCTYPE html>
<html lang="de">
<head>
<meta charset="utf-8">
<title>Banner – Fair Trade und Organic</title>
<link rel="stylesheet" href="https://fonts.googleapis.com/css2?family=Nunito:wght@800&display=swap">
<style>
  :root {
    --wall-light: #f2909b;
    --wall-mid: #ee838f;
    --wall-deep: #e67482;
    --hair: #3a2326;
    --skin: #e8b4a0;
    --shirt: #f4f2f3;
    --denim: #aab6b8;
    --ink: #262626;
  }
  html, body {
    margin: 0;
    padding: 0;
    width: 1200px;
    height: 387px;
    overflow: hidden;
  }
  .banner {
    position: relative;
    width: 1200px;
    height: 387px;
    overflow: hidden;
    background: radial-gradient(ellipse at 55% 45%, var(--wall-light) 0%, var(--wall-mid) 55%, var(--wall-deep) 100%);
  }
  .banner__photo {
    position: absolute;
    inset: 0;
    display: block;
  }
  .banner__headline {
    position: absolute;
    left: 152px;
    top: 176px;
    margin: 0;
    font-family: "Nunito", sans-serif;
    font-weight: 800;
    font-size: 39px;
    line-height: 50px;
    color: var(--ink);
    transform: rotate(-3.3deg);
    transform-origin: left top;
    white-space: nowrap;
  }
</style>
</head>
<body>
  <section class="banner">
    <svg class="banner__photo" width="1200" height="387" viewBox="0 0 1200 387" role="img" aria-label="Foto: lächelnde junge Frau im weißen T-Shirt und Latzhose vor einer pinken Wand">
      <defs>
        <linearGradient id="person-fill" x1="0" y1="0" x2="0" y2="1">
          <stop offset="0" stop-color="var(--hair)"/>
          <stop offset="0.2" stop-color="var(--skin)"/>
          <stop offset="0.34" stop-color="var(--shirt)"/>
          <stop offset="0.76" stop-color="var(--shirt)"/>
          <stop offset="0.84" stop-color="var(--denim)"/>
          <stop offset="1" stop-color="var(--denim)"/>
        </linearGradient>
      </defs>
      <rect x="812" y="40" width="162" height="360" rx="40" fill="url(#person-fill)"/>
    </svg>
    <h1 class="banner__headline">Viele Fair Trade und Organic<br>Produkte in unserem Shop.</h1>
  </section>
</body>
</html>
```